Chocolate covered bananas

“I am starting a new venture making chocolate coated frozen bananas. At start up I intend to have 4 different types:
3 will be single bananas ( Dark Chocolate, Dark chocolate with sprinkles and Dark Chocolate & Almonds) sold in individual packets, 70MM(W) x 215mm(L)

The other will be Banana Pops (smaller pieces of banana) sold in a 500g bag and then packed in a 165mm(L) x 50mm(W) X 165mm(H) cardboard box

The packaging will need my logo the wording “Chocolate Coated Frozen Banana” and the slogan “Crunchy Sunny Snack” on it. A picture of a Banana and Chocolate (The chocolate can be on the banana, getting poured on it, or even beside it).
I would like the words “Zero Trans-fat” on both the packaging (3 variations) and the 500g container along with “Healthy Dessert Treat” on the Container.

I need the Ingredients and nutritional information on the back"

one version can be submitted within the Contest period, however the winner is required to provide all 4 versions as part of the project.

Good Luck

JUST A QUICK NOTE THE BANANAS WILL BE ON A ICE-CREAM STICK AND THE BANANA POPS WILL BE ON A POPSICLE STICK.

Here are a couple of examples from places in America (no competition to me I am in another country) I'm am looking for something similar in size. as the packets in merrily mangoes and the cartons in corals kiwis. http://www.merrily-mangoes.example/products.php and http://www.coralskiwis.example/our-products/ I hope this helps Regards Gareth.

Hi I am getting some great designs Most are dark brown (or chocolate ) in colour they look good however most ice cream packs are dark and I think in order for these to stand out they need to be brighter with the chocolate as a secondary colour. Regards Gareth.

Hi all great designs it will be very hard to pick. just a quick note I made a spelling mistake in my brief it is HEALTHY DESSERT TREAT (NOT DESERT) SORRY Regards Gareth.

I would like to thank everyone for there time and effort they have put in to my packaging design contest. I am meeting with the packaging company on Thursday and will have a decision Thursday night. Regards Gareth.

Target Market(s)

I plan to go down the track that these are a healthy tasty fun treat.
I will be using real Bananas and Real chocolate.

```html
<!DOCTYPE html>
<html lang="en">
<head>
<meta charset="utf-8">
<title>Golden Grove – Dark Chocolate Packet</title>
<link rel="stylesheet" href="https://fonts.googleapis.com/css2?family=Source+Sans+3:wght@600;700;800&display=swap">
<style>
  :root {
    --canvas-bg: #e4e4e4;
    --choc-dark: #3a1208;
    --choc-mid: #6b220f;
    --choc-warm: #8c3a17;
    --pack-orange: #f39a12;
    --pack-amber: #f7b515;
    --pack-yellow: #fde51b;
    --banana-light: #f3e2a0;
    --banana-deep: #c9a14a;
    --ink: #2a150c;
  }
  * { margin: 0; padding: 0; box-sizing: border-box; }
  html, body { width: 1200px; height: 1200px; overflow: hidden; }
  body {
    background: var(--canvas-bg);
    font-family: "Source Sans 3", sans-serif;
    color: var(--ink);
    position: relative;
  }
  .packet-shape { position: absolute; left: 410px; top: 40px; }
  .brand-lockup {
    position: absolute; left: 410px; top: 312px; width: 436px;
    display: flex; align-items: center; justify-content: center; gap: 12px;
  }
  .brand-dot {
    width: 26px; height: 26px; border-radius: 50%;
    background: var(--choc-dark);
  }
  .brand-name {
    font-weight: 700; font-size: 36px; line-height: 1;
    color: var(--ink);
  }
  .slogan {
    position: absolute; left: 410px; top: 460px; width: 436px;
    text-align: center;
    font-weight: 700; font-size: 14px; letter-spacing: 2px;
    text-transform: uppercase;
  }
  .product-title {
    position: absolute; left: 410px; top: 502px; width: 436px;
    text-align: center;
    font-weight: 700; font-size: 27px; line-height: 37px;
    letter-spacing: -0.4px;
  }
  .flavour-tag {
    position: absolute; left: 507px; top: 584px;
    width: 242px; height: 37px;
    border: 2.5px solid var(--ink); border-radius: 7px;
    display: flex; align-items: center; justify-content: center;
    font-weight: 800; font-size: 23px; letter-spacing: -0.3px;
    text-transform: uppercase;
  }
  .transfat-badge {
    position: absolute; left: 588px; top: 1003px;
    width: 70px; height: 70px; border-radius: 50%;
    display: flex; flex-direction: column; align-items: center; justify-content: center;
    color: var(--pack-yellow); font-weight: 700;
  }
  .transfat-badge .label { font-size: 9px; letter-spacing: 1px; text-transform: uppercase; }
  .transfat-badge .zero { font-size: 30px; line-height: 28px; font-weight: 800; }
</style>
</head>
<body>
  <svg class="packet-shape" width="436" height="1065" viewBox="0 0 436 1065" xmlns="http://www.w3.org/2000/svg">
    <defs>
      <clipPath id="packet-outline">
        <path d="M0,12 L15,0 L31,12 L46,0 L62,12 L77,0 L93,12 L108,0 L124,12 L139,0 L155,12 L170,0 L186,12 L201,0 L217,12 L232,0 L248,12 L263,0 L279,12 L294,0 L310,12 L325,0 L341,12 L356,0 L372,12 L387,0 L403,12 L418,0 L436,12
                 L436,1053 L418,1065 L403,1053 L387,1065 L372,1053 L356,1065 L341,1053 L325,1065 L310,1053 L294,1065 L279,1053 L263,1065 L248,1053 L232,1065 L217,1053 L201,1065 L186,1053 L170,1065 L155,1053 L139,1065 L124,1053 L108,1065 L93,1053 L77,1065 L62,1053 L46,1065 L31,1053 L15,1065 L0,1053 Z"/>
      </clipPath>
      <radialGradient id="pack-glow" cx="0.5" cy="0.5" r="0.75">
        <stop offset="0" stop-color="var(--pack-yellow)"/>
        <stop offset="0.55" stop-color="var(--pack-amber)"/>
        <stop offset="1" stop-color="var(--pack-orange)"/>
      </radialGradient>
      <linearGradient id="drip-band" x1="0" y1="0" x2="0" y2="1">
        <stop offset="0" stop-color="var(--choc-dark)"/>
        <stop offset="0.55" stop-color="var(--choc-mid)"/>
        <stop offset="1" stop-color="var(--choc-warm)" stop-opacity="0"/>
      </linearGradient>
      <linearGradient id="base-band" x1="0" y1="0" x2="0" y2="1">
        <stop offset="0" stop-color="var(--choc-warm)"/>
        <stop offset="1" stop-color="var(--choc-dark)"/>
      </linearGradient>
      <radialGradient id="banana-tones" cx="0.5" cy="0.45" r="0.6">
        <stop offset="0" stop-color="var(--banana-light)"/>
        <stop offset="0.6" stop-color="var(--banana-deep)"/>
        <stop offset="1" stop-color="var(--choc-mid)" stop-opacity="0.85"/>
      </radialGradient>
    </defs>
    <g clip-path="url(#packet-outline)">
      <rect class="packet-body" width="436" height="1065" fill="url(#pack-glow)"/>
      <rect class="chocolate-drips" role="img" aria-label="Melted chocolate dripping down from the top seal" x="0" y="0" width="436" height="190" fill="url(#drip-band)"/>
      <rect class="chocolate-base" x="0" y="940" width="436" height="125" fill="url(#base-band)"/>
      <rect class="banana-illustration" role="img" aria-label="Half-peeled banana in a splash of dark chocolate with chocolate drops" x="60" y="650" width="320" height="300" rx="130" fill="url(#banana-tones)"/>
    </g>
  </svg>

  <div class="brand-lockup">
    <span class="brand-dot"></span>
    <span class="brand-name">Golden Grove</span>
  </div>

  <p class="slogan">Crunchy Sunny Snack</p>
  <h1 class="product-title">Chocolate Coated<br>Frozen Banana</h1>
  <div class="flavour-tag">Dark Chocolate</div>

  <div class="transfat-badge">
    <span class="label">Trans-fat</span>
    <span class="zero">0</span>
    <span class="label">Trans-fat</span>
  </div>
</body>
</html>
```